Design a double sided business card

We are looking for a clean, eye-catching, and contemporary design that enhances the brand and presents a premium, professional image. Our preference is for a brown card with black gloss detailing and embossed elements; however, we are open to creative input and design suggestions that best achieve a strong visual impact.

Please see the attached existing business card for reference. We use both black and brown colours consistently across our branding.

On sample provided

```html
<!DOCTYPE html>
<html lang="en">
<head>
<meta charset="utf-8">
<title>Halden Business Card</title>
<link href="https://fonts.googleapis.com/css2?family=Montserrat:wght@800&family=Roboto:wght@400;500&display=swap" rel="stylesheet">
<style>
  :root {
    --page-bg: #2b2b2b;
    --card-tan: #c8b49a;
    --ink: #111111;
    --ink-soft: #2a2a2a;
    --divider: #3a3a3a;
  }
  * { box-sizing: border-box; margin: 0; padding: 0; }
  html, body {
    width: 1200px;
    height: 880px;
    overflow: hidden;
    background: var(--page-bg);
  }
  .canvas {
    position: relative;
    width: 1200px;
    height: 880px;
  }
  .card {
    position: absolute;
    left: 285px;
    width: 630px;
    height: 360px;
    background: var(--card-tan);
    border-radius: 28px;
    color: var(--ink);
  }
  .card--front { top: 60px; }
  .card--back { top: 460px; }

  .brand {
    display: flex;
    flex-direction: column;
    align-items: center;
    gap: 18px;
  }
  .brand__square {
    width: 92px;
    height: 92px;
    background: var(--ink);
  }
  .brand__name {
    font-family: "Montserrat", sans-serif;
    font-weight: 800;
    font-size: 62px;
    letter-spacing: 6px;
    color: var(--ink);
    line-height: 1;
  }
  .card--front .brand {
    position: absolute;
    left: 0; right: 0;
    top: 76px;
  }

  .card--back .brand {
    position: absolute;
    left: 40px;
    width: 300px;
    top: 112px;
  }
  .card--back .brand__square { width: 64px; height: 64px; }
  .card--back .brand__name { font-size: 42px; letter-spacing: 4px; }

  .divider {
    position: absolute;
    left: 350px;
    top: 70px;
    width: 1.5px;
    height: 220px;
    background: linear-gradient(to bottom, transparent, var(--divider) 30%, var(--divider) 70%, transparent);
  }

  .contact {
    position: absolute;
    left: 380px;
    top: 58px;
    font-family: "Roboto", sans-serif;
    color: var(--ink-soft);
  }
  .contact__name {
    font-family: "Montserrat", sans-serif;
    font-weight: 800;
    font-size: 24px;
    color: var(--ink);
    letter-spacing: 0.5px;
  }
  .contact__role {
    font-size: 15px;
    margin: 2px 0 14px;
    color: #3b3b3b;
  }
  .contact__list { list-style: none; }
  .contact__item {
    display: flex;
    align-items: center;
    gap: 12px;
    font-size: 16px;
    height: 27px;
  }
  .contact__item svg { width: 15px; height: 15px; flex: none; }
  .contact__address {
    margin-top: 10px;
    font-size: 16px;
    line-height: 1.3;
  }
</style>
</head>
<body>
<main class="canvas">

  <section class="card card--front" aria-label="Card front">
    <div class="brand">
      <div class="brand__square"></div>
      <div class="brand__name">HALDEN</div>
    </div>
  </section>

  <section class="card card--back" aria-label="Card back">
    <div class="brand">
      <div class="brand__square"></div>
      <div class="brand__name">HALDEN</div>
    </div>

    <div class="divider"></div>

    <div class="contact">
      <h1 class="contact__name">TOM ASHBY</h1>
      <p class="contact__role">Director</p>
      <ul class="contact__list">
        <li class="contact__item">
          <svg viewBox="0 0 16 16" aria-hidden="true"><path d="M3 1.5l3 .5 1 3.5-2 1.2a8 8 0 0 0 4.3 4.3l1.2-2 3.5 1 .5 3-2 1.5C7 14 2 9 1.5 3.5z" fill="#111"/></svg>
          0800 000 4217
        </li>
        <li class="contact__item">
          <svg viewBox="0 0 16 16" aria-hidden="true"><rect x="4" y="1" width="8" height="14" rx="1.5" fill="none" stroke="#111" stroke-width="1.4"/><circle cx="8" cy="12.5" r=".9" fill="#111"/></svg>
          07700 900318
        </li>
        <li class="contact__item">
          <svg viewBox="0 0 16 16" aria-hidden="true"><rect x="1" y="3" width="14" height="10" fill="#111"/><path d="M1.5 3.5L8 9l6.5-5.5" fill="none" stroke="#c8b49a" stroke-width="1.2"/></svg>
          tom@halden.co.uk
        </li>
        <li class="contact__item">
          <svg viewBox="0 0 16 16" aria-hidden="true"><circle cx="8" cy="8" r="6.5" fill="none" stroke="#111" stroke-width="1.4"/><path d="M1.5 8h13M8 1.5c-3 3.5-3 9.5 0 13M8 1.5c3 3.5 3 9.5 0 13" fill="none" stroke="#111" stroke-width="1.1"/></svg>
          www.halden.co.uk
        </li>
      </ul>
      <p class="contact__address">12 Mill Close Lane<br>Eastbridge EB4 2QT</p>
    </div>
  </section>

</main>
</body>
</html>
```